BRAXO Pure Energy (Energy Drink) Promo Sticker Designs

We want to promote our products and brand through stickers and social a bit more. This means the 4 designs will be used in various ways, but most importantly as stickers, social banners and social posts.

There are no hard design guidelines this time, because we're looking for something out of the box (our box that is).

Company background:
We're an energy drink kind of company. Energy Formulas are powdered versions of Energy Drinks that mix a bit like supplements. First of all, we don't have an issue with edginess, but we mainly define ourselves through retro (80's/90's) gaming with a bit of a modern twist.

The owners also own a larger photo and video production company, but due to the current crisis and a lot of work coming in, we're now looking for an other solution to designing.

For some basic idea of our design we refer to @purebraxo on Instagram and/or purebraxo.example. And if you Google "K VOLT sticker" you'll see what one of our competitors is doing. There are brand and flavour specific stickers.

Use:
We just want to add a sticker to every order we and our customer FizzCrateStore gets. Besides this, they could function as temporary social banners to promote a specific product.

Basic spec:
We need a design for 4 cool looking stickers 150mm wide, 53mm high. They may be differ from sticker to sticker or they could use the same design, there is no specific guideline for this.

Please don't use Plomex templates, because we know how to work these by our selves ;).

Barcode:
The attached EAN barcode needs to be somewhere in the image (it can be placed in a shape as long as there's a 5mm hight with full width black on white, examples attached.

Basic designs:
3 product specific stickers for our flavours:
RISE AND GR*ND ON!
STAY BOLD STAY BOLD!
DIG THIS WILD ST*FF
1 global BRAXO branded sticker

Delivery:
We want to create social posts about these designs. And might use them as temporary social headers etc. Also it could be use on mock-ups or renders. Therefore we would need the end result available in original Adobe files (so layered .psd, .ai or .indd).

Other projects:
Our partner FizzCrateStore.example will need a complete revamp for their corporate identity soon. But we first want to see how this goes.

Target Market(s)

European gamers aged 25-35

Requirements
Must have
• Our target group identify themselves through these products (yes through Energy Drinks, we know, but it is true). Therefore customers feel a sense of pride towards the brand. These stickers are a way for them to show this. This is how it should feel towards the brand or flavour. Not a product spec, just a cool way to show you buy this brand.
Nice to have
• Of course everyone like more design choices, but that's stating the obvious. The size is determined by the stickers now, but a design version in 1350px by 1080px for Instagram would be cool.
Should not have
• Look like K VOLT or Trundle Energy
Look like a product brochure/flyer
A lot of text

```html
<!DOCTYPE html>
<html lang="en">
<head>
<meta charset="utf-8">
<title>BRAXO Pure Energy – Sticker Set</title>
<link rel="stylesheet" href="https://fonts.googleapis.com/css2?family=Archivo+Black&family=Archivo:wght@700;800&display=swap">
<style>
  :root {
    --page: #ffffff;
    --teal: #3a9e9f;
    --teal-pattern: #35918f;
    --brown: #321a12;
    --yellow: #fbb21a;
    --yellow-pattern: #eea514;
    --pink: #ff3a6f;
    --pink-pattern: #f23365;
    --green: #45cc4b;
    --green-pattern: #3dbd43;
    --red: #ff4433;
    --white: #ffffff;
    --ink: #1a0f0a;
    --x-red: #e8434b;
    --x-teal: #3aa0a0;
    --x-green: #41c24a;
    --x-gold: #fbb21a;
    --x-olive: #8c6a2a;
    --x-rust: #9a5a1a;
    --x-umber: #4a2a10;
    --fruit-purple: #5a3fd1;
    --fruit-lemon: #f5e62a;
    --fruit-orange: #f7a21a;
    --fruit-pink: #f7a0c4;
  }
  * { margin: 0; padding: 0; box-sizing: border-box; }
  html, body {
    width: 1200px; height: 523px; overflow: hidden;
    background: var(--page);
  }
  .sheet { position: relative; width: 1200px; height: 523px; }

  .sticker {
    position: absolute;
    width: 359px; height: 127px;
    overflow: hidden;
  }
  .sticker--teal { background: var(--teal); }
  .sticker--brown { background: var(--brown); }
  .sticker--yellow { background: var(--yellow); }
  .sticker--pink { background: var(--pink); }
  .sticker--green { background: var(--green); }

  /* Area reserved for the faint pixel-fruit background pattern */
  .pattern-field { position: absolute; inset: 0; }
  .sticker--teal .pattern-field { background: linear-gradient(180deg, var(--teal) 0%, var(--teal-pattern) 100%); }
  .sticker--yellow .pattern-field { background: linear-gradient(180deg, var(--yellow) 0%, var(--yellow-pattern) 100%); }
  .sticker--pink .pattern-field { background: linear-gradient(180deg, var(--pink) 0%, var(--pink-pattern) 100%); }
  .sticker--green .pattern-field { background: linear-gradient(180deg, var(--green) 0%, var(--green-pattern) 100%); }

  /* Brand lockup */
  .lockup {
    position: absolute; left: 0; right: 0; top: 0; bottom: 6px;
    display: flex; align-items: center; justify-content: center; gap: 7px;
  }
  .lockup__name {
    font-family: "Archivo Black", sans-serif;
    font-size: 44px; line-height: 1; letter-spacing: -0.5px;
  }
  .lockup__tagline {
    font-family: "Archivo", sans-serif; font-weight: 800;
    font-size: 19px; line-height: 0.92; letter-spacing: 0.3px;
  }
  .lockup__tagline span { display: block; }

  .c-white { color: var(--white); }
  .c-yellow { color: var(--yellow); }
  .c-red { color: var(--red); }
  .c-pink { color: var(--pink); }
  .c-teal { color: var(--teal); }

  /* Flavour slogan */
  .slogan {
    position: absolute; left: 62px; top: 18px;
    font-family: "Archivo Black", sans-serif;
    font-size: 29px; line-height: 1.08; letter-spacing: -0.3px;
    color: var(--white);
    -webkit-text-stroke: 1px var(--ink);
    text-transform: uppercase;
  }
  .slogan span { display: block; white-space: nowrap; }
  .slogan__second { padding-left: 50px; }
  .slogan--rise {
    text-shadow: 1px 1px 0 var(--ink), 2px 2px 0 var(--x-red), 3px 3px 0 var(--ink), 4px 4px 0 var(--x-teal),
                 5px 5px 0 var(--ink), 6px 6px 0 var(--x-green), 7px 7px 0 var(--ink), 8px 8px 0 var(--x-red),
                 9px 9px 0 var(--ink), 10px 10px 0 var(--x-green), 11px 11px 0 var(--ink);
  }
  .slogan--dig {
    text-shadow: 1px 1px 0 var(--ink), 2px 2px 0 var(--x-gold), 3px 3px 0 var(--ink), 4px 4px 0 var(--x-teal),
                 5px 5px 0 var(--ink), 6px 6px 0 var(--x-olive), 7px 7px 0 var(--ink), 8px 8px 0 var(--x-gold),
                 9px 9px 0 var(--ink), 10px 10px 0 var(--x-teal), 11px 11px 0 var(--ink);
  }
  .slogan--stay {
    text-shadow: 1px 1px 0 var(--ink), 2px 2px 0 var(--x-gold), 3px 3px 0 var(--ink), 4px 4px 0 var(--x-rust),
                 5px 5px 0 var(--ink), 6px 6px 0 var(--x-gold), 7px 7px 0 var(--ink), 8px 8px 0 var(--x-umber),
                 9px 9px 0 var(--ink), 10px 10px 0 var(--x-rust), 11px 11px 0 var(--ink);
  }

  .fruit-cluster {
    position: absolute; top: 40px;
    width: 42px; height: 40px; border-radius: 6px;
  }
  .fruit-cluster--left { left: 18px; }
  .fruit-cluster--right { right: 20px; }
  .fruit--grape-lemon { background: linear-gradient(135deg, var(--fruit-purple), var(--fruit-lemon)); }
  .fruit--peach-carrot { background: linear-gradient(135deg, var(--fruit-pink), var(--fruit-orange)); }
  .fruit--pineapple-lemon { background: linear-gradient(135deg, var(--fruit-orange), var(--fruit-lemon)); }
</style>
</head>
<body>
<main class="sheet">

  <!-- Column 1 -->
  <section class="sticker sticker--teal" style="left:35px; top:45px;">
    <div class="pattern-field" role="img" aria-label="Faint pixel fruit pattern"></div>
    <div class="lockup"><span class="lockup__name c-white">BRAXO</span><span class="lockup__tagline"><span class="c-red">PURE</span><span class="c-yellow">ENERGY</span></span></div>
  </section>

  <section class="sticker sticker--brown" style="left:37px; top:206px;">
    <div class="lockup"><span class="lockup__name c-white">BRAXO</span><span class="lockup__tagline"><span class="c-red">PURE</span><span class="c-yellow">ENERGY</span></span></div>
  </section>

  <section class="sticker sticker--teal" style="left:40px; top:347px;">
    <div class="pattern-field" role="img" aria-label="Faint pixel fruit pattern"></div>
    <div class="lockup"><span class="lockup__name c-yellow">BRAXO</span><span class="lockup__tagline"><span class="c-red">PURE</span><span class="c-yellow">ENERGY</span></span></div>
  </section>

  <!-- Column 2 -->
  <section class="sticker sticker--brown" style="left:426px; top:47px;">
    <div class="lockup"><span class="lockup__name c-yellow">BRAXO</span><span class="lockup__tagline"><span class="c-teal">PURE</span><span class="c-yellow">ENERGY</span></span></div>
  </section>

  <section class="sticker sticker--teal" style="left:419px; top:196px;">
    <div class="pattern-field" role="img" aria-label="Faint pixel fruit pattern"></div>
    <div class="lockup"><span class="lockup__name c-white">BRAXO</span><span class="lockup__tagline"><span class="c-pink">PURE</span><span class="c-yellow">ENERGY</span></span></div>
  </section>

  <section class="sticker sticker--brown" style="left:419px; top:352px;">
    <div class="lockup"><span class="lockup__name c-white">BRAXO</span><span class="lockup__tagline"><span class="c-pink">PURE</span><span class="c-teal">ENERGY</span></span></div>
  </section>

  <!-- Column 3: flavour stickers -->
  <section class="sticker sticker--yellow" style="left:806px; top:47px;">
    <div class="pattern-field" role="img" aria-label="Faint pixel fruit pattern"></div>
    <div class="fruit-cluster fruit-cluster--left fruit--grape-lemon" role="img" aria-label="Pixel grape and lemon icons"></div>
    <h2 class="slogan slogan--rise"><span>Rise and</span><span class="slogan__second">Gr*nd on!</span></h2>
    <div class="fruit-cluster fruit-cluster--right fruit--grape-lemon" role="img" aria-label="Pixel grape and lemon icons"></div>
  </section>

  <section class="sticker sticker--pink" style="left:806px; top:209px;">
    <div class="pattern-field" role="img" aria-label="Faint pixel fruit pattern"></div>
    <div class="fruit-cluster fruit-cluster--left fruit--peach-carrot" role="img" aria-label="Pixel peach and carrot icons"></div>
    <h2 class="slogan slogan--dig"><span>Dig this</span><span class="slogan__second">Wild st*ff</span></h2>
    <div class="fruit-cluster fruit-cluster--right fruit--peach-carrot" role="img" aria-label="Pixel peach and carrot icons"></div>
  </section>

  <section class="sticker sticker--green" style="left:806px; top:365px;">
    <div class="pattern-field" role="img" aria-label="Faint pixel fruit pattern"></div>
    <div class="fruit-cluster fruit-cluster--left fruit--pineapple-lemon" role="img" aria-label="Pixel pineapple and lemon icons"></div>
    <h2 class="slogan slogan--stay"><span>Stay bold</span><span class="slogan__second">Stay bold!</span></h2>
    <div class="fruit-cluster fruit-cluster--right fruit--pineapple-lemon" role="img" aria-label="Pixel pineapple and lemon icons"></div>
  </section>

</main>
</body>
</html>
```